ebook (Thriller) sucht Cover
Zielgruppe
Das ebook ist für eine spannungsinteressierte Zielgruppe konzipiert. Handlungsorientiert (Action), weniger klassischer Detektivroman. Politisch-militärische Verwicklungen in der Nebenhandlung. Handlungszeitpunkt ist die Gegenwart. Lovestory ebenfalls am Rande.
Aufgabenstellung
Autorenname "Jonas Berwald“ (mit Zeilenumbruch zwischen Vor- und Nachname) ungefähr über das obere Drittel (links), moderne, schnörkellose Schrift.
Buchtitel "Nachtgrenze" groß über unteres Buchdrittel, die komplette Breite einnehmend (mit vernünftigem Abstand zum Rand), gleichfalls in moderner, technischer Schrift.
Blutige Fußabdrücke/-spuren erkennbar menschlichen Ursprungs im rechten Coverbereich vertikal.
Genre „Thriller“, wie bei solchen Büchern üblich, mittig (in geringer Schriftgröße) über unterem Buchrand.
Hintergrund mit grau und weiß oder beige. (siehe Beispielbilder)
Covergestaltung muss auch in kleinem Format (100 oder 160px in der Breite) noch in wenigen Augenblicken erfassbar sein.

```html
<!DOCTYPE html>
<html lang="de">
<head>
<meta charset="utf-8">
<title>Jonas Berwald – Nachtgrenze</title>
<link rel="stylesheet" href="https://fonts.googleapis.com/css2?family=Inter:wght@800&family=Rubik+Dirt&display=swap">
<style>
  :root {
    --concrete-light: #ece9e3;
    --concrete-mid: #d6d2cb;
    --concrete-dark: #a9a6a1;
    --ink: #161417;
    --rust-dark: #1c0d06;
    --rust-mid: #4a2410;
    --rust-light: #7a4a2a;
    --blood: #d8141a;
  }
  html, body {
    margin: 0;
    padding: 0;
    overflow: hidden;
    background: var(--concrete-mid);
  }
  .cover {
    position: relative;
    width: 800px;
    height: 1200px;
    overflow: hidden;
  }
  .cover-backdrop {
    position: absolute;
    inset: 0;
    background:
      radial-gradient(ellipse 40% 30% at 45% 0%, rgba(90, 90, 95, 0.35), transparent 70%),
      radial-gradient(ellipse 35% 30% at 30% 85%, rgba(90, 88, 85, 0.3), transparent 70%),
      linear-gradient(160deg, var(--concrete-light) 0%, var(--concrete-mid) 55%, var(--concrete-dark) 100%);
  }
  .blood-prints {
    position: absolute;
    left: 474px;
    top: 858px;
    width: 326px;
    height: 342px;
    background: radial-gradient(ellipse 55% 50% at 60% 50%, rgba(216, 20, 26, 0.85), rgba(216, 20, 26, 0.35) 60%, transparent 80%);
  }
  .author {
    position: absolute;
    left: 76px;
    top: 96px;
    margin: 0;
    font-family: "Inter", sans-serif;
    font-weight: 800;
    font-size: 82px;
    line-height: 76px;
    letter-spacing: -1px;
    color: var(--ink);
    text-transform: uppercase;
  }
  .author span { display: block; }
  .title {
    position: absolute;
    left: 0;
    top: 0;
    width: 800px;
    height: 1200px;
  }
  .title text {
    font-family: "Rubik Dirt", "Impact", sans-serif;
    font-size: 250px;
  }
  .genre {
    position: absolute;
    left: 89px;
    top: 1092px;
    margin: 0;
    font-family: "Inter", sans-serif;
    font-weight: 800;
    font-size: 47px;
    letter-spacing: 0.5px;
    color: var(--ink);
    text-transform: uppercase;
  }
</style>
</head>
<body>
<main class="cover">
  <div class="cover-backdrop" role="img" aria-label="Rissige, graue Betonwand als Hintergrund"></div>
  <div class="blood-prints" role="img" aria-label="Blutiger Handabdruck mit Spritzern rechts unten"></div>

  <h2 class="author"><span>Jonas</span><span>Berwald</span></h2>

  <svg class="title" viewBox="0 0 800 1200" aria-labelledby="book-title">
    <title id="book-title">Nachtgrenze</title>
    <defs>
      <linearGradient id="rust-fill" x1="0" y1="0" x2="1" y2="1">
        <stop offset="0" stop-color="var(--rust-light)"/>
        <stop offset="0.35" stop-color="var(--rust-mid)"/>
        <stop offset="1" stop-color="var(--rust-dark)"/>
      </linearGradient>
    </defs>
    <text x="54" y="658" textLength="601" lengthAdjust="spacingAndGlyphs" fill="url(#rust-fill)">NACHT</text>
    <text x="79" y="867" textLength="672" lengthAdjust="spacingAndGlyphs" fill="url(#rust-fill)">GRENZE</text>
  </svg>

  <p class="genre">Thriller</p>
</main>
</body>
</html>
```